TARO PTY LTD - Business Cards

Design a modern business card - using the attached Designs.
Same design as on the front, apart from the names/numbers/emails to be different.
We want the cards to be very glossy to stand out, do I think the simple black/white/metallic will be effective.
Both lots of details below:

Lyle Marrick
Director
lyle_taro@quintmail.example
0493 628 304

Simon Prowle
Director
simon_taro@quintmail.example
0438 514 209

```html
<!DOCTYPE html>
<html lang="en">
<head>
<meta charset="utf-8">
<title>TARO PTY LTD – Business Cards</title>
<link href="https://fonts.googleapis.com/css2?family=Bitter:wght@400;600&display=swap" rel="stylesheet">
<style>
  :root {
    --stage: #e9e7e4;
    --card-front: #2b3237;
    --card-back: #1e1f21;
    --glow: #c9cbcc;
    --ink-light: #d9dcde;
    --band-light: #b9bcbe;
    --band-dark: #6b6f72;
  }
  * { margin: 0; padding: 0; box-sizing: border-box; }
  html, body { width: 1200px; height: 457px; overflow: hidden; }
  body {
    background: var(--stage);
    font-family: "Bitter", Georgia, serif;
    position: relative;
  }
  .card {
    position: absolute;
    top: 62px;
    width: 550px;
    height: 333px;
    overflow: hidden;
    box-shadow: 0 6px 18px rgba(0,0,0,.25);
  }
  .card--front { left: 35px; background: var(--card-front); }
  .card--back {
    left: 615px;
    background: radial-gradient(ellipse 48% 62% at 50% 50%, var(--glow) 0%, #8d9092 45%, var(--card-back) 100%);
  }
  .brand {
    position: absolute;
    left: 0; right: 0;
    display: flex;
    align-items: center;
    justify-content: center;
    gap: 12px;
    color: var(--ink-light);
    font-weight: 600;
    letter-spacing: 2px;
  }
  .brand__dot {
    border-radius: 50%;
    background: var(--ink-light);
  }
  .card--front .brand { top: 66px; font-size: 26px; }
  .card--front .brand__dot { width: 18px; height: 18px; }
  .card--back .brand { top: 142px; font-size: 38px; color: #2b2d2f; }
  .card--back .brand__dot { width: 26px; height: 26px; background: #2b2d2f; }
  .contact {
    position: absolute;
    top: 190px;
    left: 0; right: 0;
    text-align: center;
    color: var(--ink-light);
    font-size: 15px;
    line-height: 1.5;
  }
  .contact__name { margin-bottom: 16px; }
  .contact__line { display: flex; justify-content: center; align-items: center; gap: 7px; font-size: 15.5px; }
  .contact__line svg { width: 12px; height: 12px; fill: var(--ink-light); }
  .band { position: absolute; left: 0; bottom: 0; width: 550px; height: 70px; }
</style>
</head>
<body>
  <section class="card card--front">
    <div class="brand"><span class="brand__dot"></span>TARO PTY LTD</div>
    <div class="contact">
      <p class="contact__name">Simon Prowle, Director</p>
      <p class="contact__line">
        <svg viewBox="0 0 16 16" aria-hidden="true"><path d="M3.6 1.2l2.3 2.6-1.3 1.7c.9 2 2.5 3.6 4.5 4.5l1.7-1.3 2.6 2.3-1.4 2.3C7 13.3 2.7 9 2.2 3z"/></svg>
        0438 514 209
      </p>
      <p class="contact__line">
        <svg viewBox="0 0 16 16" aria-hidden="true"><path d="M1 4h14v9H1z M1 4l7 5 7-5" fill="none" stroke="#d9dcde" stroke-width="1.6"/></svg>
        simon_taro@quintmail.example
      </p>
    </div>
    <svg class="band" viewBox="0 0 550 70" preserveAspectRatio="none" aria-hidden="true">
      <polygon points="0,62 300,62 325,40 550,20 550,70 0,70" fill="var(--band-dark)"/>
      <polygon points="290,62 318,36 550,8 550,20 325,42 305,62" fill="var(--band-light)"/>
    </svg>
  </section>

  <section class="card card--back">
    <div class="brand"><span class="brand__dot"></span>TARO PTY LTD</div>
  </section>
</body>
</html>
```